We are looking for a Flyer we will send through the mail for residents of Apartment Buildings

We are a laundry service doing pickup and delivery for the Manhattan Area.
We offer next day delivery on all laundry orders.
we want to send out a flyer to buildings for unbelievable promotion:

50% your first order (coupon code FOLD50)
2nd order FREE! (up to $50)
FREE pickup and delivery
FREE next day service
FREE Brisa and Plumo
schedule now on www.quickrinsehub.com!

We offer the cleanest and brightest laundry in the city!
Attached is our logo plus some icons to use

Target Market(s)

females ages 24-40

Industry/Entity Type

Apartment

Font styles to use
Other font styles liked:
• habraba

Requirements
Must have
• modern and clean look
• our logo
• BRIGHT COLORS
• Size of flyer will be 8.52 x 5.47
• Logo font: Harabara
• Slogan font: Swiss 721 Light Extended BT
• Dark blue: C 100 M 88 Y 0 K 0
• Light blue: C 85 M 50 Y 0 K 0
• Orange: C 0 M 80 Y 95 K 0
• Violet: C 85 M 100 Y 0 K 0
Should not have
• we dont want to be too busy

```html
<!DOCTYPE html>
<html lang="en">
<head>
<meta charset="utf-8">
<title>quickrinsehub.com — Laundry Pickup &amp; Delivery</title>
<link rel="stylesheet" href="https://fonts.googleapis.com/css2?family=Lato:wght@300;400;700;900&family=Dancing+Script:wght@700&display=swap">
<style>
  :root {
    --dark-blue: #2b3a9c;
    --violet: #3d2a91;
    --light-blue: #2a9fd8;
    --band: #3db8da;
    --band-deep: #2fa9cc;
    --orange: #f04e23;
    --grey: #6b6b6b;
    --white: #ffffff;
  }
  * { box-sizing: border-box; margin: 0; padding: 0; }
  html, body { width: 776px; height: 1200px; overflow: hidden; background: var(--white); }
  .flyer {
    position: relative; width: 776px; height: 1200px;
    font-family: "Lato", "Helvetica Neue", Arial, sans-serif; color: var(--dark-blue);
  }
  .abs { position: absolute; }
  .script { font-family: "Dancing Script", cursive; font-weight: 700; }

  .offer-rule { top: 72px; height: 1px; background: var(--dark-blue); width: 210px; }
  .offer-label {
    top: 56px; left: 0; width: 776px; text-align: center;
    font-weight: 300; font-size: 27px; letter-spacing: 1px; color: var(--dark-blue);
  }
  .headline {
    top: 102px; left: 0; width: 776px; text-align: center;
    font-weight: 300; font-size: 33px; color: var(--dark-blue);
  }
  .headline .script { font-size: 37px; color: var(--violet); }

  .brand { top: 290px; left: 0; width: 776px; text-align: center; }
  .brand-name {
    display: inline-flex; align-items: center; gap: 10px;
    font-weight: 900; font-size: 32px; color: var(--dark-blue);
  }
  .brand-dot { width: 22px; height: 22px; border-radius: 50%; background: var(--light-blue); }
  .brand-slogan { margin-top: 2px; font-size: 11px; letter-spacing: 1px; color: var(--orange); }

  .services { top: 403px; left: 0; width: 776px; height: 393px;
    background: linear-gradient(180deg, var(--band-deep) 0%, var(--band) 12%, var(--band) 100%); }
  .service { position: absolute; top: 70px; width: 230px; text-align: center; color: var(--white); }
  .service svg { display: block; margin: 0 auto; }
  .service-title { margin-top: 10px; font-weight: 700; font-size: 27px; line-height: 32px; }
  .service-text { margin-top: 6px; font-size: 17px; line-height: 21px; }

  .promo-title {
    top: 823px; left: 0; width: 776px; text-align: center;
    font-weight: 300; font-size: 28px; color: var(--dark-blue);
  }
  .promo-title .script { font-size: 33px; color: var(--violet); }

  .discount-tag { left: 91px; top: 896px; }
  .first-order { left: 250px; top: 898px; width: 115px; text-align: center; }
  .first-order-title { font-weight: 700; font-size: 21px; line-height: 26px; color: var(--light-blue); }
  .coupon { margin-top: 6px; font-size: 15px; line-height: 19px; color: var(--grey); }
  .divider { left: 375px; top: 900px; width: 1px; height: 86px; background: var(--light-blue); }
  .second-order { left: 390px; top: 898px; width: 115px; text-align: center; color: var(--orange); }
  .second-order-title { font-weight: 700; font-size: 21px; line-height: 24px; }
  .second-order-title sup { font-size: 12px; }
  .second-order-free { font-weight: 900; font-size: 36px; line-height: 38px; }
  .second-order-cap { font-size: 15px; }
  .ampersand { left: 508px; top: 916px; font-size: 44px; color: var(--dark-blue); }
  .freebies { left: 555px; top: 905px; font-size: 16px; line-height: 20px; color: var(--light-blue); }
  .freebies strong { color: var(--orange); font-weight: 700; }

  .cta-box {
    left: 91px; top: 1043px; width: 340px; height: 97px;
    border: 2px solid var(--band); text-align: center; padding-top: 16px;
  }
  .cta-lead { font-weight: 300; font-size: 22px; color: var(--dark-blue); }
  .cta-url { font-weight: 700; font-size: 27px; color: var(--light-blue); margin-top: 2px; }

  .standards { left: 445px; top: 1026px; width: 264px; text-align: center;
    font-size: 16px; line-height: 21px; color: var(--dark-blue); }
  .partners { left: 458px; top: 1098px; width: 240px; display: flex; align-items: center; justify-content: space-between; }
  .partner-name { font-weight: 700; font-size: 18px; color: var(--dark-blue); }
  .partner-chip { display: flex; align-items: center; gap: 5px; }
  .partner-dot { width: 14px; height: 14px; border-radius: 50%; background: var(--orange); }
  .badge-square { width: 36px; height: 36px; background: var(--dark-blue); border-radius: 4px; }
  .badge-circle { width: 40px; height: 40px; background: var(--light-blue); border-radius: 50%; }
</style>
</head>
<body>
<main class="flyer">
  <div class="abs offer-rule" style="left:100px"></div>
  <div class="abs offer-rule" style="left:466px"></div>
  <p class="abs offer-label">WE OFFER</p>
  <h1 class="abs headline">the <span class="script">cleanest</span> and <span class="script">brightest laundry</span> in the city!</h1>

  <div class="abs brand">
    <div class="brand-name"><span class="brand-dot"></span>quickrinsehub.com</div>
    <p class="brand-slogan">Cleaner. Brighter. Faster.</p>
  </div>

  <section class="abs services">
    <div class="service" style="left:58px">
      <svg width="100" height="110" viewBox="0 0 100 110" aria-hidden="true">
        <path d="M50 2a48 48 0 0 1 16 93L50 108 34 95A48 48 0 0 1 50 2z" fill="var(--white)"/>
        <circle cx="50" cy="50" r="40" fill="var(--band)"/>
        <circle cx="50" cy="50" r="35" fill="none" stroke="var(--white)" stroke-width="3"/>
        <circle cx="50" cy="52" r="16" fill="none" stroke="var(--white)" stroke-width="4"/>
        <path d="M50 44v9h6" stroke="var(--white)" stroke-width="3" fill="none" stroke-linecap="round"/>
        <circle cx="37" cy="35" r="5" fill="var(--white)"/><circle cx="63" cy="35" r="5" fill="var(--white)"/>
        <path d="M40 68l-4 5M60 68l4 5" stroke="var(--white)" stroke-width="3" stroke-linecap="round"/>
      </svg>
      <h2 class="service-title">Schedule<br>Pick up</h2>
      <p class="service-text">Easy Online Access<br>24 Hour Turnaround.</p>
    </div>
    <div class="service" style="left:274px">
      <svg width="100" height="110" viewBox="0 0 100 110" aria-hidden="true">
        <path d="M50 2a48 48 0 0 1 16 93L50 108 34 95A48 48 0 0 1 50 2z" fill="var(--white)"/>
        <circle cx="50" cy="50" r="40" fill="var(--band)"/>
        <circle cx="50" cy="50" r="35" fill="none" stroke="var(--white)" stroke-width="3"/>
        <path d="M50 26a4 4 0 1 1 0 6v4M30 44l20-8 20 8-6 8-4-2v20H40V50l-4 2z" fill="none" stroke="var(--white)" stroke-width="3" stroke-linejoin="round"/>
        <path d="M44 56l10 10" stroke="var(--white)" stroke-width="3"/>
      </svg>
      <h2 class="service-title">We pick up<br>wash and fold</h2>
      <p class="service-text">5 Star Rated Laundry<br>Service</p>
    </div>
    <div class="service" style="left:501px">
      <svg width="100" height="110" viewBox="0 0 100 110" aria-hidden="true">
        <path d="M50 2a48 48 0 0 1 16 93L50 108 34 95A48 48 0 0 1 50 2z" fill="var(--white)"/>
        <circle cx="50" cy="50" r="40" fill="var(--band)"/>
        <circle cx="50" cy="50" r="35" fill="none" stroke="var(--white)" stroke-width="3"/>
        <path d="M27 38h28v22H27zM55 45h10l7 8v7H55z" fill="none" stroke="var(--white)" stroke-width="3" stroke-linejoin="round"/>
        <circle cx="35" cy="63" r="4" fill="var(--white)"/><circle cx="64" cy="63" r="4" fill="var(--white)"/>
        <path d="M41 38v22M27 49h28" stroke="var(--white)" stroke-width="2"/>
      </svg>
      <h2 class="service-title">Next Day<br>Delivery</h2>
      <p class="service-text">On All Laundry<br>Orders</p>
    </div>
  </section>

  <p class="abs promo-title">we bring to <span class="script">you</span> this <span class="script">unbelievable promotion</span> :</p>

  <svg class="abs discount-tag" width="158" height="108" viewBox="0 0 158 108" aria-label="50% off">
    <polygon points="0,14 150,0 158,92 8,108" fill="var(--light-blue)"/>
    <polygon points="150,0 158,92 140,96 132,4" fill="#1b82bd"/>
    <text x="12" y="76" font-family="Lato, sans-serif" font-weight="900" font-size="58" fill="var(--white)">50</text>
    <text x="84" y="52" font-family="Lato, sans-serif" font-weight="900" font-size="32" fill="var(--white)">%</text>
    <text x="86" y="78" font-family="Lato, sans-serif" font-weight="900" font-size="20" fill="var(--white)">OFF</text>
  </svg>
  <div class="abs first-order">
    <p class="first-order-title">Your First<br>Order</p>
    <p class="coupon">coupon code:<br>FOLD50</p>
  </div>
  <div class="abs divider"></div>
  <div class="abs second-order">
    <p class="second-order-title">2<sup>nd</sup> order</p>
    <p class="second-order-free">FREE!</p>
    <p class="second-order-cap">(up to $50)</p>
  </div>
  <span class="abs ampersand script">&amp;</span>
  <div class="abs freebies">
    <p><strong>FREE:</strong></p>
    <p>Pickup and Delivery</p>
    <p>Next Day Service</p>
    <p>Brisa and Plumo</p>
  </div>

  <div class="abs cta-box">
    <p class="cta-lead">schedule now on</p>
    <p class="cta-url">www.quickrinsehub.com!</p>
  </div>

  <p class="abs standards">We use Premium Detergents and Leading Industry Standards</p>
  <div class="abs partners">
    <span class="partner-name">Plumo</span>
    <span class="partner-chip"><span class="partner-dot"></span><span class="partner-name">Brisa</span></span>
    <span class="badge-square" role="img" aria-label="Fabric certification badge"></span>
    <span class="badge-circle" role="img" aria-label="Environmental certification badge"></span>
  </div>
</main>
</body>
</html>
```